Popup Banners - BrightCounsel - Legal Technology

- We need two banners (same style) designed with two different images and different text.

- The details of the printing requirements are attached, along with suggested images.

- The banners should share the same theme as our website www.brightcounsel.com.au

- The first banner would include our logo (attached), use the 'roads join' image (attached) in some way and text: New Opportunities - Where legal services and technology meet.

- The second banner would include our logo (attached), use the 'jigsaw' image (attached) in some way and use text: Legal Technology Strategy, Advice and Capability.

- Details on what are required from the Printer is attached also.

Target Market(s)

Legal Professionals

Industry/Entity Type

Information Technology

Font styles to use
Sans Serif

Requirements
Must have
• Our logo (attached), suggested text and the image mentioned for each.
Nice to have
• Professional and modern look
Should not have
• Cheap looking

```html
<!DOCTYPE html>
<html lang="en">
<head>
<meta charset="utf-8">
<title>BrightCounsel Popup Banners</title>
<link rel="stylesheet" href="https://fonts.googleapis.com/css2?family=Jost:ital,wght@0,300;0,400;0,500;1,300;1,400&display=swap">
<style>
  :root {
    --page: #ffffff;
    --banner-bg: #ffffff;
    --outline: #3a3a3a;
    --charcoal: #5a524e;
    --brand-blue: #5b9fd2;
    --mark-blue: #4f9ad3;
    --text-light: #ffffff;
  }
  html, body {
    margin: 0;
    padding: 0;
    width: 1200px;
    height: 1051px;
    overflow: hidden;
    background: var(--page);
  }
  .canvas {
    position: relative;
    width: 1200px;
    height: 1051px;
  }
  .banner {
    position: absolute;
    top: 70px;
    width: 382px;
    height: 918px;
    background: var(--banner-bg);
    outline: 1px solid var(--outline);
  }
  .banner--strategy { left: 138px; }
  .banner--opportunities { left: 606px; }
  .banner svg {
    display: block;
    width: 100%;
    height: 100%;
    font-family: "Jost", sans-serif;
  }
  .brand-name {
    font-weight: 500;
    font-size: 22px;
    letter-spacing: 3px;
    fill: var(--charcoal);
  }
  .brand-square { fill: var(--mark-blue); }
  .band { fill: var(--brand-blue); }
  .arc { fill: var(--charcoal); }
  .headline {
    fill: var(--text-light);
    font-weight: 300;
  }
  .headline--italic { font-style: italic; }
  .contact {
    fill: var(--text-light);
    font-weight: 300;
  }
  .address {
    fill: var(--text-light);
    font-weight: 300;
    font-size: 10.5px;
    opacity: 0.9;
  }
</style>
</head>
<body>
<main class="canvas">

  <section class="banner banner--strategy">
    <svg viewBox="0 0 326 783" preserveAspectRatio="none">
      <defs>
        <radialGradient id="jigsaw-tone" cx="0.62" cy="0.55" r="0.7">
          <stop offset="0" stop-color="#e8f4ff"/>
          <stop offset="0.3" stop-color="#8fc3ea"/>
          <stop offset="0.7" stop-color="#2f6fa3"/>
          <stop offset="1" stop-color="#0f3558"/>
        </radialGradient>
        <clipPath id="clip-strategy">
          <rect x="0" y="140" width="326" height="500"/>
        </clipPath>
      </defs>

      <rect class="brand-square" x="40" y="46" width="20" height="20"/>
      <text class="brand-name" x="68" y="65">BrightCounsel</text>

      <rect class="band" x="0" y="500" width="326" height="283"/>
      <ellipse class="arc" cx="163" cy="376" rx="218" ry="259"/>
      <ellipse role="img" aria-label="Photo of a hand fitting a glowing blue jigsaw puzzle piece"
               clip-path="url(#clip-strategy)" fill="url(#jigsaw-tone)"
               cx="163" cy="375" rx="210" ry="236"/>

      <text class="headline headline--italic" x="305" y="340" text-anchor="end" font-size="16">Legal Technology Strategy,</text>
      <text class="headline" x="307" y="370" text-anchor="end" font-size="28">Advice &amp; Capability</text>

      <text class="contact" x="25" y="674"><tspan font-size="15">Contact us on </tspan><tspan font-size="19">07 4100 2288</tspan></text>
      <text class="address" x="25" y="697">Level 9, 120 Harbour Lane Brisbane QLD, Australia</text>
    </svg>
  </section>

  <section class="banner banner--opportunities">
    <svg viewBox="0 0 326 783" preserveAspectRatio="none">
      <defs>
        <linearGradient id="roads-tone" x1="0" y1="0" x2="0" y2="1">
          <stop offset="0" stop-color="#2f7fc4"/>
          <stop offset="0.2" stop-color="#8cc1e6"/>
          <stop offset="0.26" stop-color="#7fa24e"/>
          <stop offset="0.6" stop-color="#5d8c34"/>
          <stop offset="1" stop-color="#47722a"/>
        </linearGradient>
      </defs>

      <rect class="brand-square" x="40" y="46" width="20" height="20"/>
      <text class="brand-name" x="68" y="65">BrightCounsel</text>

      <rect class="band" x="0" y="500" width="326" height="283"/>
      <ellipse class="arc" cx="163" cy="376" rx="218" ry="259"/>
      <ellipse role="img" aria-label="Photo of two dirt roads joining on a grassy hill under a blue sky"
               fill="url(#roads-tone)" cx="163" cy="355" rx="212" ry="225"/>

      <text class="headline headline--italic" x="163" y="170" text-anchor="middle" font-size="15">NEW OPPORTUNITIES</text>
      <text class="headline headline--italic" x="163" y="188" text-anchor="middle" font-size="15">Where legal services and technology</text>
      <text class="headline" x="163" y="214" text-anchor="middle" font-size="24">come together</text>

      <text class="contact" x="25" y="674"><tspan font-size="15">Contact us on </tspan><tspan font-size="19">07 4100 2288</tspan></text>
      <text class="address" x="25" y="697">Level 9, 120 Harbour Lane Brisbane QLD, Australia</text>
    </svg>
  </section>

</main>
</body>
</html>
```